Task Dossier:

Client: Wrenfield Orbit Sprouts (WOS)
Due Date: Sept 21 2022
Project: Wrenfield Orbit Sprouts (WOS) New Website Pages

Brand Guideline: There is no brand guidelines document. Please mirro the colors and fonts you see in the mock-up and here is the WOS website. See website https://bazaar.wosplayden.com/
Copy: We are re-doing the copy so you can use placeholder text.
Website Instructions: See the mock-ups in the document named WOS Mock Up for posting on sketchtorra. You will find page mock ups and instructions in Red in the document. There is a landing page and 3 additional pages that are intended to rotate on a carousel. And then there are pages that can be accessed by the navigation provided.
Industry: child edu-tainment. WOS is a company focused on “doing good” in various communities
Format: We expect to create this website in Wix so requirement is to make the graphics Wix compatible

Task: This is an exciting and revolutionary opportunity for WOS’s NFT portfolio, creating another revenue stream for non-profit organizations so we want to make pages creatively communicate this. Additionally we want the graphics to elicit trust and brand recognition. The wireframes and other websites provided are meant to be directional. We encourage you to provide your best ideas, using the guidelines provided.

There is no brand guidelines document. Please mirro the colors and fonts you see in the mock-up and here is the WOS website. See website https://bazaar.wosplayden.com/
See the mock-ups in the document named WOS Mock Up for posting on sketchtorra. You will find page mock ups and instructions in Red in the document. There is a landing page and 3 additional pages that are intended to rotate on a carousel. And then there are pages that can be accessed by the navigation provided.
VIsuals should be engaging but not too distracting.
Leverage the WOS logo and other graphics we provided
We are open to all other images and overall design, while maintaining the colors and typography stated. Please be creative but again professional and demonstrate that WOS is a company focused on doing good in various communities

```html
<!DOCTYPE html>
<html lang="en">
<head>
<meta charset="utf-8">
<title>WOS Website Hero Carousel</title>
<link href="https://fonts.googleapis.com/css2?family=Poppins:wght@600;700&family=Roboto:wght@300;500;700&family=Yellowtail&display=swap" rel="stylesheet">
<style>
  :root {
    --board: #c4c4c4;
    --white: #ffffff;
    --gold: #f7c515;
    --blue: #1d55ad;
    --overlay: rgba(20, 22, 30, 0.45);
    --photo-a: #7a6a58;
    --photo-b: #4f5d74;
    --photo-c: #b9a78c;
    --photo-d: #d8d3c6;
  }
  * { box-sizing: border-box; margin: 0; padding: 0; }
  html, body { width: 960px; height: 1200px; overflow: hidden; }
  body { background: var(--board); position: relative; font-family: "Roboto", sans-serif; }

  .hero {
    position: absolute; left: 60px; width: 840px; height: 480px; overflow: hidden;
    box-shadow: 0 4px 18px rgba(0,0,0,0.25);
  }
  .hero--welcome { top: 89px; }
  .hero--ticket { top: 631px; }

  .hero__photo {
    position: absolute; inset: 0;
    background:
      radial-gradient(ellipse at 50% 95%, var(--photo-d) 0%, transparent 55%),
      radial-gradient(ellipse at 20% 60%, var(--photo-b) 0%, transparent 45%),
      radial-gradient(ellipse at 80% 55%, var(--photo-c) 0%, transparent 50%),
      linear-gradient(180deg, #5b4a3a 0%, var(--photo-a) 45%, #9a907f 100%);
  }
  .hero__photo::after { content: ""; position: absolute; inset: 0; background: var(--overlay); }

  .brand { position: absolute; left: 78px; top: 16px; width: 80px; text-align: center; color: var(--white); }
  .brand__mark {
    width: 78px; height: 78px; border-radius: 50%; background: var(--blue);
    border: 2px solid var(--white);
    display: flex; align-items: center; justify-content: center;
    font-family: "Poppins", sans-serif; font-weight: 700; font-size: 20px;
  }
  .brand__partner { margin-top: 10px; font-family: "Poppins", sans-serif; font-weight: 600; line-height: 1; text-align: left; padding-left: 2px; }
  .brand__partner small { display: block; font-size: 5px; }
  .brand__partner span { font-size: 12px; }

  .nav { position: absolute; top: 23px; left: 379px; display: flex; align-items: center; gap: 6px;
    font-weight: 500; font-size: 10px; color: var(--white); }
  .nav__star { color: var(--gold); font-size: 7px; }
  .nav__caret { font-size: 7px; margin-left: 1px; }

  .hero__content { position: absolute; left: 0; right: 0; text-align: center; color: var(--white); }
  .hero__script { font-family: "Yellowtail", cursive; color: var(--gold); font-size: 28px; line-height: 1; }
  .hero__title { font-family: "Poppins", sans-serif; font-weight: 700; font-size: 35px; line-height: 36px; }
  .hero__lead { font-family: "Poppins", sans-serif; font-weight: 600; font-size: 11px; line-height: 18px; }
  .hero__tag { font-weight: 300; font-size: 14px; color: var(--gold); }

  .btn {
    position: absolute; left: 367px; width: 106px; height: 30px; border-radius: 15px;
    background: var(--blue); color: var(--white); font-weight: 700; font-size: 10px;
    display: flex; align-items: center; justify-content: center; gap: 3px;
  }

  .follow { position: absolute; left: 78px; top: 411px; color: var(--white); font-size: 10px; }
  .social { position: absolute; left: 78px; top: 437px; display: flex; gap: 3px; }
  .social span { width: 23px; height: 23px; border-radius: 50%; border: 1.5px solid var(--white); }

  .ticket-art {
    position: absolute; left: 370px; top: 116px; width: 102px; height: 98px; border-radius: 6px;
    background: linear-gradient(135deg, #f6d33a, #d9a812);
    border: 2px solid #b48a10;
  }
</style>
</head>
<body>

<section class="hero hero--welcome">
  <div class="hero__photo" role="img" aria-label="Children and a teacher gathered around a table with maps and atlases in a library"></div>
  <div class="brand">
    <div class="brand__mark">WOS</div>
    <div class="brand__partner"><small>Powered by</small><span>Vaultline</span></div>
  </div>
  <nav class="nav">
    <span>Home</span><span class="nav__star">★</span>
    <span>WOS NFTs</span><span class="nav__star">★</span>
    <span>WOS Scholarships<span class="nav__caret">⌄</span></span><span class="nav__star">★</span>
    <span>About WOS<span class="nav__caret">⌄</span></span><span class="nav__star">★</span>
    <span>Contact us</span><span class="nav__star">★</span>
    <span>Help</span>
  </nav>
  <div class="hero__content" style="top:144px;">
    <p class="hero__script">Welcome to</p>
    <h1 class="hero__title" style="margin-top:12px;">The Home of WOS NFTs and<br>the WOS Golden Ticket!</h1>
    <p class="hero__lead" style="margin-top:20px;">WOS NFTs...<br>Not just a vanity purchase but an investment in long-term opportunity!</p>
  </div>
  <a class="btn" style="top:329px;">LEARN MORE <svg width="9" height="9" viewBox="0 0 10 10"><circle cx="5" cy="5" r="5" fill="#fff"/><path d="M4 2.8 6.2 5 4 7.2" stroke="#1d55ad" stroke-width="1.6" fill="none"/></svg></a>
  <p class="follow">Follow us :</p>
  <div class="social" aria-label="Social links"><span></span><span></span><span></span><span></span></div>
</section>

<section class="hero hero--ticket">
  <div class="hero__photo" role="img" aria-label="Children and a teacher gathered around a table with maps and atlases in a library"></div>
  <div class="brand">
    <div class="brand__mark">WOS</div>
    <div class="brand__partner"><small>Powered by</small><span>Vaultline</span></div>
  </div>
  <nav class="nav">
    <span>Home</span><span class="nav__star">★</span>
    <span>WOS NFTs</span><span class="nav__star">★</span>
    <span>WOS Scholarships<span class="nav__caret">⌄</span></span><span class="nav__star">★</span>
    <span>About WOS<span class="nav__caret">⌄</span></span><span class="nav__star">★</span>
    <span>Contact us</span><span class="nav__star">★</span>
    <span>Help</span>
  </nav>
  <div class="ticket-art" role="img" aria-label="Illustrated commemorative golden ticket with cartoon characters"></div>
  <div class="hero__content" style="top:226px;">
    <h1 class="hero__title" style="font-size:36px;">WOS Commemorative Golden<br>Ticket NFTs</h1>
    <p class="hero__tag" style="margin-top:6px;">A limited, special collection of 100 NFTs</p>
  </div>
  <a class="btn" style="top:352px;">LEARN MORE <svg width="9" height="9" viewBox="0 0 10 10"><circle cx="5" cy="5" r="5" fill="#fff"/><path d="M4 2.8 6.2 5 4 7.2" stroke="#1d55ad" stroke-width="1.6" fill="none"/></svg></a>
  <p class="follow">Follow us :</p>
  <div class="social" aria-label="Social links"><span></span><span></span><span></span><span></span></div>
</section>

</body>
</html>
```